Fernvale Pantry web design

Go to fernvalepantry.com.au an using the current layout create a design that will attract customers to this wholefood website.

You may suggest / make slight changes to the layout to create effective graphic design principles.

The LOGO design is TM already. So no changes there. Second logo attached is authorised for use and is a area branding LOGO.

Colours need to reflect health and wellbeing.

Don't want Medical style or New age.
Updates

Logo now loaded

Thank you for your submissions so far. I have sent them out to a trusty panel of friends to hear what they have to say. Some of you have done very well.

Project Deadline Extended
Reason: There are a few submissions outstanding. I will eliminate a few designs today and give feed back. Thankyou

Thank you for your submissions so far I will not be asking for more design submissions from other designers. The ones I have are under consideration and there are a few minor changes to each that may just bring out the one that is IT! The two designs I have narrowed it down to are very different in approach so please bear with me a couple more days. Thank you.

Target Market(s)

Whole food health concious people target market locally Home Delivery would be young Mums with restricted movement because of young children. Older people that are restricted transport users.

Busy commuters that leave our area for work and just want to relax on the weekend with their family and local bush walking or garden activities.

Industry/Entity Type

Graphic Design

Requirements
Should not have
• Medical or sterile hospital feel. New age or too alternative living feel.

```html
<!DOCTYPE html>
<html lang="en">
<head>
<meta charset="utf-8">
<title>Fernvale Pantry</title>
<link href="https://fonts.googleapis.com/css2?family=Raleway:wght@500;600&family=Open+Sans:wght@400;600;700&family=Oswald:wght@400;500&display=swap" rel="stylesheet">
<style>
:root{
  --purple:#5a1466;
  --purple-mid:#8e2a94;
  --purple-light:#b457b8;
  --lime:#8fe01a;
  --green:#5aa51c;
  --green-dark:#3f7e10;
  --red:#d8121b;
  --ink:#222;
  --muted:#666;
  --card:#f1f1f1;
  --footer:#2b2b2b;
  --page-top:#ffffff;
  --page-bottom:#f6e4f6;
}
*{box-sizing:border-box;margin:0;padding:0}
html,body{width:937px;height:1200px;overflow:hidden}
body{position:relative;font-family:"Open Sans",sans-serif;color:var(--ink);
  background:linear-gradient(180deg,var(--page-top) 0,var(--page-top) 380px,var(--page-bottom) 700px,var(--page-bottom) 100%)}
.topbar{position:absolute;left:0;top:0;width:937px;height:48px;background:var(--purple)}
.logo{position:absolute;left:83px;top:8px;width:141px;height:86px;border-radius:50%;background:#fff;border:4px solid var(--purple);display:flex;align-items:center;justify-content:center;flex-direction:column;gap:2px}
.logo-dot{width:14px;height:14px;border-radius:50%;background:var(--green)}
.logo-name{font-family:"Open Sans",sans-serif;font-weight:700;font-size:13px;color:var(--purple)}
.main-nav{position:absolute;top:0;left:0;height:48px;width:937px}
.main-nav a{position:absolute;top:13px;height:25px;line-height:25px;font-family:"Open Sans",sans-serif;font-weight:700;font-size:10.5px;color:#fff;text-decoration:none;transform:translateX(-50%);white-space:nowrap}
.main-nav a.active{background:var(--lime);color:var(--purple);padding:0 11px;border-radius:2px}
.main-nav .sep{position:absolute;top:6px;width:1px;height:36px;background:rgba(255,255,255,.18)}
.call{position:absolute;left:472px;top:70px;width:198px;height:32px;border-bottom:1px dashed #888;display:flex;align-items:center;gap:6px;font-family:"Oswald",sans-serif}
.call svg{flex:none}
.call-label{font-size:14px;color:#222}
.call-number{font-size:16px;color:var(--purple-mid)}
.cart{position:absolute;left:692px;top:68px;width:165px;height:38px;border:1px solid #ccc;border-radius:4px;background:#fff;display:flex;align-items:center;padding:0 6px;gap:6px}
.cart-text{font-family:"Oswald",sans-serif;font-size:10.5px;line-height:12px;color:#333}
.checkout{margin-left:auto;background:var(--red);color:#fff;font-family:"Open Sans",sans-serif;font-weight:600;font-size:9.5px;padding:5px 5px;border-radius:4px}
.slider{position:absolute;left:78px;top:130px;width:780px;height:320px;border:5px solid #2a2a2a;background:#2a2a2a}
.slider-photo{position:absolute;inset:0;background:linear-gradient(135deg,#c9a63b 0,#b03b2b 35%,#7c3a2a 55%,#c8c4b6 80%,#e8e4e0 100%)}
.slider-caption{position:absolute;left:33px;top:42px;width:560px;height:66px;background:rgba(0,0,0,.28);padding:8px 16px;font-family:"Raleway",sans-serif;font-weight:600;font-size:20px;line-height:26px;color:#fff}
.slider-arrow{position:absolute;top:136px;width:18px;height:20px;display:flex;align-items:center;justify-content:center;background:rgba(0,0,0,.45)}
.slider-arrow.prev{left:0}.slider-arrow.next{right:0}
.sidebar{position:absolute;left:82px;top:484px;width:180px}
.side-title{font-family:"Raleway",sans-serif;font-weight:500;font-size:18px;color:var(--purple)}
.side-list{list-style:none;margin-top:6px}
.side-list li{font-size:10.5px;line-height:23.4px}
.side-list li::before{content:"• ";font-size:8px}
.side-list.weight li{font-size:11.5px;line-height:25px}
.side-title.weight{margin-top:22px}
.divider{position:absolute;left:273px;top:480px;width:1px;height:600px;background:#d9c3d9}
.section-bar{position:absolute;left:289px;width:569px;height:40px;border-radius:6px 6px 0 0;background:linear-gradient(180deg,var(--purple-light),var(--purple-mid));padding:3px}
.section-bar span{display:block;height:100%;border:1px dashed rgba(255,255,255,.8);border-radius:4px 4px 0 0;font-family:"Raleway",sans-serif;font-weight:600;font-size:17px;color:#fff;line-height:32px;padding-left:16px}
.card{position:absolute;width:164px;height:210px;background:var(--card);border-radius:6px;padding:3px}
.card-inner{height:100%;border:1px dashed #999;border-radius:4px;padding:9px 8px 0}
.card-title{font-weight:600;font-size:12px;line-height:14px}
.card-sub{font-size:8.5px;color:var(--muted);margin-top:3px}
.card-photo{margin-top:6px;height:96px;background:#fff;border:1px solid #e2e2e2;padding:4px}
.card-photo div{width:100%;height:100%}
.photo-seeds{background:linear-gradient(135deg,#b39c92,#8a6f66 50%,#c4b1a8)}
.photo-jar{background:radial-gradient(circle at 50% 50%,#7a4a2a 0,#7a4a2a 18px,#fff 19px)}
.photo-nuts{background:linear-gradient(135deg,#b8844c,#8c5a2c 50%,#c59560)}
.card-price{text-align:center;font-size:16px;color:var(--purple-mid);margin-top:6px}
.buy{display:block;margin:4px auto 0;width:67px;height:22px;border-radius:2px;background:linear-gradient(180deg,#6fbf22,var(--green-dark));color:#fff;font-weight:600;font-size:11px;line-height:22px;text-align:center}
.footer{position:absolute;left:0;top:1104px;width:937px;height:96px;background:var(--footer);border-top:3px solid var(--green)}
.footer-nav{position:absolute;left:78px;top:10px;font-size:8.5px;color:#fff;word-spacing:1px}
.footer-nav span{margin:0 5px}
.copyright{position:absolute;left:78px;top:28px;font-size:8.5px;color:#fff}
.pay{position:absolute;left:78px;top:55px;display:flex;gap:6px}
.pay i{display:block;width:26px;height:16px;border-radius:2px;background:#d5d5d5}
.pay i.wide{width:62px;background:#bdbdbd}
.area-badge{position:absolute;left:724px;top:12px;width:112px;height:66px;border-radius:4px;background:#444}
</style>
</head>
<body>
<header>
  <div class="topbar"></div>
  <nav class="main-nav">
    <a class="active" style="left:273px">HOME</a>
    <span class="sep" style="left:318px"></span>
    <a style="left:356px">SHOP</a>
    <span class="sep" style="left:395px"></span>
    <a style="left:484px">PURCHASE BY WEIGHT</a>
    <span class="sep" style="left:569px"></span>
    <a style="left:620px">RECIPES</a>
    <span class="sep" style="left:670px"></span>
    <a style="left:710px">BLOG</a>
    <span class="sep" style="left:755px"></span>
    <a style="left:812px">CONTACT US</a>
  </nav>
  <div class="logo"><span class="logo-dot"></span><span class="logo-name">Fernvale Pantry</span></div>
  <div class="call">
    <svg width="20" height="20" viewBox="0 0 20 20"><rect width="20" height="20" rx="2" fill="#5aa51c"/><path d="M6 4c1 0 2 2.5 2 3s-1 1-1 1.5 2 3.5 3.5 3.5c.5 0 1-1 1.5-1s3 1 3 2-1.5 2.5-2.5 2.5C9 15.5 4.5 11 4.5 6.5 4.5 5.5 5 4 6 4z" fill="#fff"/></svg>
    <span class="call-label">CALL US:</span>
    <span class="call-number">1 800 555 0142</span>
  </div>
  <div class="cart">
    <svg width="30" height="24" viewBox="0 0 30 24"><path d="M1 3h5l3 12h15l3-9H8" fill="none" stroke="#5aa51c" stroke-width="2.5"/><circle cx="11" cy="20" r="2" fill="#5aa51c"/><circle cx="22" cy="20" r="2" fill="#5aa51c"/></svg>
    <div class="cart-text">MY CART:<br>(0 ITEMS)</div>
    <span class="checkout">CHECKOUT</span>
  </div>
</header>

<section class="slider">
  <div class="slider-photo" role="img" aria-label="Grocery store aisle with shelves of packaged goods"></div>
  <div class="slider-caption">This nut butter has absolutely no additives.<br>Just Australian Peanuts.</div>
  <span class="slider-arrow prev"><svg width="8" height="10" viewBox="0 0 8 10"><path d="M6 1 2 5l4 4" fill="none" stroke="#fff" stroke-width="2"/></svg></span>
  <span class="slider-arrow next"><svg width="8" height="10" viewBox="0 0 8 10"><path d="M2 1l4 4-4 4" fill="none" stroke="#fff" stroke-width="2"/></svg></span>
</section>

<aside class="sidebar">
  <h2 class="side-title">Product Categories</h2>
  <ul class="side-list">
    <li>Alternative goods</li><li>Dairy Free</li><li>Gluten Free</li><li>Grocery</li><li>Health Supplements</li><li>Natural Grocer</li><li>Organic</li><li>Recipes</li><li>Seasonal</li><li>Sugar Replacements</li>
  </ul>
  <h2 class="side-title weight">By Weight Categories</h2>
  <ul class="side-list weight">
    <li>Baking</li><li>Beans &amp; Peas</li><li>Candy &amp; Sweet Treats</li><li>Cereals &amp; Granolas</li><li>Coffee &amp; Tea</li><li>Dried Fruit</li><li>Flour</li><li>Free Range Meat</li><li>Gluten Free Processed Meat</li><li>Candy &amp; Sweet Treats</li>
  </ul>
</aside>
<div class="divider"></div>

<main>
  <h2 class="section-bar" style="top:478px"><span>Latest Deals</span></h2>
  <article class="card" style="left:290px;top:542px"><div class="card-inner"><div class="card-title">Cat Nap</div><div class="card-sub">Cat nap bags for baby</div><div class="card-photo"><div class="photo-seeds" role="img" aria-label="Mixed seeds"></div></div><div class="card-price">$ 50.20</div><span class="buy">Buy Now</span></div></article>
  <article class="card" style="left:491px;top:542px"><div class="card-inner"><div class="card-title">Cat Nap</div><div class="card-sub">Cat nap bags for baby</div><div class="card-photo"><div class="photo-jar" role="img" aria-label="Supplement jar"></div></div><div class="card-price">$ 50.20</div><span class="buy">Buy Now</span></div></article>
  <article class="card" style="left:690px;top:542px"><div class="card-inner"><div class="card-title">Cat Nap</div><div class="card-sub">Cat nap bags for baby</div><div class="card-photo"><div class="photo-nuts" role="img" aria-label="Pile of almonds"></div></div><div class="card-price">$ 50.20</div><span class="buy">Buy Now</span></div></article>

  <h2 class="section-bar" style="top:782px"><span>Latest News</span></h2>
  <article class="card" style="left:290px;top:846px"><div class="card-inner"><div class="card-title">Cat Nap</div><div class="card-sub">Cat nap bags for baby</div><div class="card-photo"><div class="photo-seeds" role="img" aria-label="Mixed seeds"></div></div><div class="card-price">$ 50.20</div><span class="buy">Buy Now</span></div></article>
  <article class="card" style="left:491px;top:846px"><div class="card-inner"><div class="card-title">Cat Nap</div><div class="card-sub">Cat nap bags for baby</div><div class="card-photo"><div class="photo-jar" role="img" aria-label="Supplement jar"></div></div><div class="card-price">$ 50.20</div><span class="buy">Buy Now</span></div></article>
  <article class="card" style="left:690px;top:846px"><div class="card-inner"><div class="card-title">Cat Nap</div><div class="card-sub">Cat nap bags for baby</div><div class="card-photo"><div class="photo-nuts" role="img" aria-label="Pile of almonds"></div></div><div class="card-price">$ 50.20</div><span class="buy">Buy Now</span></div></article>
</main>

<footer class="footer">
  <div class="footer-nav">HOME<span>|</span>SHOP<span>|</span>PURCHASE BY WEIGHT<span>|</span>RECIPES<span>|</span>BLOG<span>|</span>CONTACT US</div>
  <div class="copyright">© 2014 Fernvale Pantry Company.&nbsp; All rights reserved.&nbsp; Privacy Policy&nbsp; |&nbsp; Terms of Use</div>
  <div class="pay" aria-label="Accepted payment methods"><i></i><i></i><i></i><i></i><i></i><i class="wide"></i></div>
  <div class="area-badge" role="img" aria-label="Area sustainable business badge"></div>
</footer>
</body>
</html>
```